brisk-vale.com Real Estate, Investment, Financial corporate

Real Estate, Investment, Financial corporate looking site. Show present a professional firm, with an elegant display. Please see the attached file which includes the logo, palette and fonts.
Updates

We just starting the brief today. ( logo was delayed)

Target Market(s)

Investors, Corporate , B2b

Industry/Entity Type

real-estate investments

Number of Pages Required

3 page

Requirements
Must have
• Dazzling Homepage
Nice to have
• paralex

```html
<!DOCTYPE html>
<html lang="en">
<head>
<meta charset="utf-8">
<title>Brisk Vale Group — Real Estate Investment</title>
<link rel="stylesheet" href="https://fonts.googleapis.com/css2?family=Libre+Baskerville:wght@400;700&family=Poppins:wght@400;500;600&display=swap">
<style>
:root{
  --ink:#232323;
  --ink-2:#2b2b2b;
  --gold:#f3c98b;
  --gold-soft:#f7dcb1;
  --gold-deep:#e9b56b;
  --paper:#ffffff;
  --mist:#efefef;
  --text:#3a3a3a;
  --muted:#8a8a8a;
  --serif:'Libre Baskerville', Georgia, serif;
  --sans:'Poppins', Arial, sans-serif;
}
*{box-sizing:border-box;margin:0;padding:0}
html,body{width:1200px;height:4539px;overflow:hidden;background:var(--paper)}
body{font-family:var(--sans);color:var(--text);position:relative}
.abs{position:absolute}
.page{position:relative;width:1200px;height:4539px;overflow:hidden}

/* shared */
.eyebrow{font-family:var(--sans);font-weight:600;font-size:12px;letter-spacing:.3px;color:var(--ink);text-transform:uppercase;display:flex;align-items:center;gap:12px}
.eyebrow::after{content:"";width:34px;height:1px;background:#bdbdbd}
.eyebrow.centered::before{content:"";width:34px;height:1px;background:#bdbdbd}
.section-title{font-family:var(--serif);font-weight:700;font-size:32px;color:var(--gold);text-transform:uppercase;letter-spacing:.5px;line-height:1.15;white-space:nowrap}
.btn{position:absolute;display:flex;align-items:center;justify-content:center;font-size:10px;font-weight:600;letter-spacing:.3px;text-transform:uppercase}
.btn.dark{background:var(--ink);color:var(--gold);box-shadow:3px 3px 0 -1px var(--paper),4px 4px 0 0 var(--gold)}
.btn.gold{background:var(--gold);color:var(--ink);box-shadow:3px 3px 0 -1px var(--paper),4px 4px 0 0 var(--ink)}
.photo{position:absolute}

/* header + hero */
.hero-band{left:0;top:0;width:1200px;height:606px;background:var(--ink)}
.brand{display:flex;align-items:center;gap:12px;color:var(--gold)}
.brand-mark{width:44px;height:44px;border:2px solid var(--gold)}
.brand-name{font-family:var(--serif);font-size:27px;line-height:1}
.brand-sub{font-family:var(--sans);font-size:8px;letter-spacing:2px;text-align:right;margin-top:2px}
.nav a{position:absolute;top:39px;font-size:12px;color:#d8d8d8;text-decoration:none;letter-spacing:.4px}
.nav a.current{color:var(--gold);font-weight:600}
.search{left:1055px;top:30px;width:34px;height:33px;border:2px solid var(--gold);display:flex;align-items:center;justify-content:center}
.hero-title{left:109px;top:126px;font-family:var(--serif);font-weight:700;font-size:50px;line-height:56px;color:#fff}
.hero-sub{left:110px;top:245px;font-size:13px;color:#e2e2e2}
.deco-frame{left:706px;top:106px;width:494px;height:500px;border:16px solid #3d3a34;border-right:none}
.deco-inner{left:860px;top:222px;width:210px;height:384px;border:14px solid #3d3a34;border-bottom:none}
.slide-arrow{width:39px;height:39px;background:#fff;display:flex;align-items:center;justify-content:center;box-shadow:0 2px 8px rgba(0,0,0,.15)}

/* about */
.about-frame{left:210px;top:958px;width:373px;height:376px;border:2px solid var(--gold)}
.about-frame2{left:221px;top:969px;width:352px;height:355px;border:1px solid var(--gold)}
.about-text{left:654px;top:994px;width:345px}
.about-text .section-title{font-size:31px;letter-spacing:0;line-height:37px;margin-top:6px}
.about-text p{font-size:10.5px;line-height:21px;color:#777;margin-top:16px}

/* team */
.team-band{left:0;top:1413px;width:1200px;height:358px;background:var(--mist)}
.team-dark{left:805px;top:1413px;width:395px;height:358px;background:var(--ink)}
.team-deco{left:1090px;top:1640px;width:110px;height:131px;border:10px solid #3d3a34;border-right:none;border-bottom:none}
.arrow-btn{width:31px;height:30px;border:2px solid #bdbdbd;display:flex;align-items:center;justify-content:center}
.arrow-btn.on{border-color:var(--gold)}
.member{position:absolute;top:1559px;width:233px;height:298px;background:#fff;border:1px solid #e2e2e2;box-shadow:0 4px 10px rgba(0,0,0,.05)}
.member .photo{left:4px;top:5px;width:223px;height:244px}
.member .name{position:absolute;left:0;bottom:0;width:100%;height:50px;display:flex;align-items:center;justify-content:center;font-size:12px;font-weight:600;color:var(--ink);text-transform:uppercase}
.member.active{background:var(--gold);border-color:var(--gold)}

/* portfolio */
.tile{position:absolute}
.overlay{position:absolute;left:117px;top:2566px;width:302px;height:199px;background:rgba(38,38,38,.88);color:#fff;text-align:center}
.overlay h3{font-family:var(--serif);font-size:15px;font-weight:700;margin-top:40px;letter-spacing:.5px}
.overlay p{font-size:10px;line-height:17px;color:#cfcfcf;margin:6px 26px 0}
.overlay .more{position:absolute;left:86px;top:126px;width:134px;height:32px;border:2px solid #fff;display:flex;align-items:center;justify-content:center;font-size:10px;font-weight:600;letter-spacing:.4px}

/* news */
.news-band{left:0;top:2932px;width:1200px;height:645px;background:var(--mist)}
.post{position:absolute;top:3082px;width:243px;height:350px;background:#fff}
.post .photo{left:0;top:0;width:243px;height:209px}
.post .date{position:absolute;left:21px;top:231px;height:23px;padding:0 12px;background:var(--ink);color:#fff;font-size:9px;font-weight:500;display:flex;align-items:center}
.post .date.gold{background:var(--gold);color:var(--ink)}
.post h4{position:absolute;left:21px;top:272px;width:210px;font-family:var(--serif);font-size:13px;line-height:21px;color:var(--ink)}
.post .read{position:absolute;left:21px;top:316px;font-size:10px;font-weight:600;color:var(--ink);text-decoration:underline;display:flex;align-items:center;gap:10px}
.post .read.gold{color:var(--gold)}

/* contact */
.form-box{left:210px;top:3765px;width:502px;height:305px;background:linear-gradient(135deg,var(--gold-soft),var(--gold) 55%,var(--gold-deep))}
.field{position:absolute;height:33px;border:1px solid rgba(255,255,255,.45);background:rgba(255,255,255,.08);color:#fff;font-size:10px;padding:0 10px;display:flex;align-items:center}
.field.message{height:74px;align-items:flex-start;padding-top:10px}
.contact-frame{left:650px;top:3679px;width:439px;height:441px;border:2px solid var(--gold)}
.contact-frame2{left:661px;top:3690px;width:418px;height:420px;border:1px solid var(--gold)}

/* footer */
.footer{left:0;top:4188px;width:1200px;height:351px;background:var(--ink);color:#cfcfcf}
.footer h5{position:absolute;top:76px;font-family:var(--serif);font-size:16px;font-weight:700;color:#fff}
.footer .col-list{position:absolute;font-size:10px;line-height:26px;color:#cfcfcf;list-style:none}
.contact-row{position:absolute;left:409px;display:flex;gap:12px;font-size:10px;line-height:16px}
.social{position:absolute;top:4329px;width:30px;height:30px;background:var(--gold)}
.news-input{position:absolute;left:856px;width:233px;height:39px;border:1px solid #555;font-size:10px;color:#cfcfcf;display:flex;align-items:center;padding-left:13px}
.legal{position:absolute;top:4510px;font-size:10px;color:#cfcfcf}
</style>
</head>
<body>
<div class="page">

  <!-- Header and hero -->
  <div class="abs hero-band"></div>
  <div class="abs deco-frame"></div>
  <div class="abs deco-inner"></div>

  <div class="abs brand" style="left:109px;top:24px">
    <div class="brand-mark"></div>
    <div>
      <div class="brand-name">Brisk Vale</div>
      <div class="brand-sub">GROUP</div>
    </div>
  </div>

  <nav class="nav">
    <a class="current" style="left:467px">HOME</a>
    <a style="left:553px">ABOUT US</a>
    <a style="left:664px">PORTFOLIO</a>
    <a style="left:784px">TEAM</a>
    <a style="left:867px">NEWS</a>
    <a style="left:953px">CONTACT US</a>
  </nav>
  <div class="abs search">
    <svg width="15" height="15" viewBox="0 0 16 16" fill="none" stroke="#f3c98b" stroke-width="1.8"><circle cx="6.5" cy="6.5" r="5"/><line x1="10.3" y1="10.3" x2="15" y2="15"/></svg>
  </div>

  <h1 class="abs hero-title">Best Real<br>Estate Investment</h1>
  <p class="abs hero-sub">We are Residential, Commercial and Corporate Real Estate Investment.</p>
  <div class="btn gold" style="left:109px;top:282px;width:170px;height:46px;font-size:11px">Contact Us Now</div>

  <div class="photo" role="img" aria-label="City skyline with downtown towers under a blue sky"
       style="left:109px;top:379px;width:980px;height:498px;background:linear-gradient(180deg,#6f9fd4 0%,#a9c6e6 35%,#b99a72 62%,#6f5a44 100%)"></div>
  <div class="abs slide-arrow" style="left:90px;top:585px">
    <svg width="18" height="12" viewBox="0 0 18 12" fill="none" stroke="#f3c98b" stroke-width="1.6"><line x1="17" y1="6" x2="1" y2="6"/><polyline points="6,1 1,6 6,11"/></svg>
  </div>
  <div class="abs slide-arrow" style="left:1070px;top:585px">
    <svg width="18" height="12" viewBox="0 0 18 12" fill="none" stroke="#9a9a9a" stroke-width="1.6"><line x1="1" y1="6" x2="17" y2="6"/><polyline points="12,1 17,6 12,11"/></svg>
  </div>

  <!-- About -->
  <div class="abs about-frame"></div>
  <div class="abs about-frame2"></div>
  <div class="photo" role="img" aria-label="Glass office building with trees at its base"
       style="left:229px;top:980px;width:335px;height:333px;background:linear-gradient(160deg,#e9f1f8 0%,#7fb1da 40%,#3d76a8 70%,#c9cfd2 100%)"></div>
  <div class="abs about-text">
    <div class="eyebrow">About Us</div>
    <h2 class="section-title">Welcome to<br>BriskVale Group</h2>
    <p>Lorem ipsum dolor sit amet, consectetur adipiscing elit. Nam consequat, libero eget sollicitudin sagittis, sapien nulla ultrices elit, ac bibendum lacus ante ut ante. Praesent placerat odio libero volutpat, ut efficitur nibh euismod. Aenean ullamcorper vehicula elit, a congue turpis gravida eget. Mauris porttitor est pellentesque ultricies eget quis diam.</p>
  </div>
  <div class="btn dark" style="left:655px;top:1251px;width:134px;height:41px">Learn More</div>

  <!-- Team -->
  <div class="abs team-band"></div>
  <div class="abs team-dark"></div>
  <div class="abs team-deco"></div>
  <div class="abs" style="left:109px;top:1478px">
    <div class="eyebrow">Our Team</div>
    <h2 class="section-title" style="margin-top:4px">Meet Our Team</h2>
  </div>
  <div class="abs arrow-btn" style="left:1013px;top:1492px">
    <svg width="16" height="12" viewBox="0 0 16 12" fill="none" stroke="#cfcfcf" stroke-width="1.6"><line x1="15" y1="6" x2="1" y2="6"/><polyline points="6,1 1,6 6,11"/></svg>
  </div>
  <div class="abs arrow-btn on" style="left:1057px;top:1492px">
    <svg width="16" height="12" viewBox="0 0 16 12" fill="none" stroke="#f3c98b" stroke-width="1.6"><line x1="1" y1="6" x2="15" y2="6"/><polyline points="10,1 15,6 10,11"/></svg>
  </div>

  <div class="member" style="left:109px">
    <div class="photo" role="img" aria-label="Portrait of team member in a dark suit" style="background:linear-gradient(180deg,#9b9b9b,#6c6c6c 60%,#2e3140)"></div>
    <div class="name">Martin Hale</div>
  </div>
  <div class="member" style="left:359px">
    <div class="photo" role="img" aria-label="Portrait of team member in a white blouse" style="background:linear-gradient(180deg,#dcdcdc,#c9c2bd 55%,#f2f2f2)"></div>
    <div class="name">Nora Pell</div>
  </div>
  <div class="member active" style="left:608px">
    <div class="photo" role="img" aria-label="Portrait of team member in a grey suit" style="background:linear-gradient(180deg,#a3a3a3,#8a8a8a 55%,#5b5e6e)"></div>
    <div class="name">Owen Marsh</div>
  </div>
  <div class="member" style="left:856px">
    <div class="photo" role="img" aria-label="Portrait of team member in a cream top" style="background:linear-gradient(180deg,#bdbdbd,#b8aaa1 55%,#efe4da)"></div>
    <div class="name">Lena Brook</div>
  </div>
  <div class="btn gold" style="left:516px;top:1894px;width:164px;height:40px">Meet Our Team</div>

  <!-- Portfolio -->
  <div class="abs" style="left:0;top:2018px;width:1200px;text-align:center">
    <div class="eyebrow centered" style="justify-content:center">See Our Work</div>
    <h2 class="section-title" style="margin-top:4px">Our Portfolio</h2>
  </div>
  <div class="tile" role="img" aria-label="Glass office block at dusk" style="left:109px;top:2099px;width:317px;height:199px;background:linear-gradient(180deg,#8aa2c2,#3c4c62 55%,#b08a5c)"></div>
  <div class="tile" role="img" aria-label="Modern white villa with pool" style="left:440px;top:2099px;width:318px;height:199px;background:linear-gradient(180deg,#c9dcef,#eeeeee 50%,#4e5a52)"></div>
  <div class="tile" role="img" aria-label="Tall glass tower against the sky" style="left:772px;top:2099px;width:317px;height:444px;background:linear-gradient(160deg,#dfeaf4,#8bb4d6 45%,#2e5f86 80%,#7e9a86)"></div>
  <div class="tile" role="img" aria-label="Row of suburban family houses" style="left:109px;top:2312px;width:649px;height:231px;background:linear-gradient(180deg,#7fb2e3,#bcd6ee 40%,#b39a7c 70%,#6f7b55)"></div>
  <div class="tile" role="img" aria-label="Commercial building" style="left:109px;top:2558px;width:317px;height:214px;background:linear-gradient(180deg,#6d7c8e,#3d4a5a)"></div>
  <div class="overlay">
    <h3>COMMERCIAL</h3>
    <p>Lorem ipsum dolor sit consectetur adipiscing elit. Nam consequat, libero eget sollicitudin sagittis, sapien nulla.</p>
    <div class="more">VIEW MORE</div>
  </div>
  <div class="tile" role="img" aria-label="White villa with palm trees and pool" style="left:440px;top:2558px;width:318px;height:214px;background:linear-gradient(180deg,#a9c9e4,#f2f2f2 50%,#4f87b0)"></div>
  <div class="tile" role="img" aria-label="Apartment block with wooden balconies" style="left:772px;top:2558px;width:317px;height:214px;background:linear-gradient(180deg,#2f6fb3,#6a8fb4 45%,#b07848)"></div>
  <div class="btn dark" style="left:532px;top:2807px;width:132px;height:40px">View All</div>

  <!-- News -->
  <div class="abs news-band"></div>
  <div class="abs" style="left:0;top:2998px;width:1200px;text-align:center">
    <div class="eyebrow centered" style="justify-content:center">Our News</div>
    <h2 class="section-title" style="margin-top:4px">Our Latest News</h2>
  </div>
  <article class="post" style="left:210px">
    <div class="photo" role="img" aria-label="Stacks of coins beside a small model house" style="background:linear-gradient(180deg,#2e4466,#6b7b92 45%,#d1a760 80%,#f0f0f0)"></div>
    <div class="date">15 AUG</div>
    <h4>Nullam interdum turpis vitae risus vestibulum.</h4>
    <a class="read">READ MORE <svg width="16" height="10" viewBox="0 0 16 10" fill="none" stroke="#232323" stroke-width="1.5"><line x1="0" y1="5" x2="15" y2="5"/><polyline points="10,1 15,5 10,9"/></svg></a>
  </article>
  <article class="post" style="left:478px">
    <div class="photo" role="img" aria-label="Couple meeting an agent indoors" style="background:linear-gradient(180deg,#8b8274,#d8d2c8 50%,#e9e6e1)"></div>
    <div class="date gold">07 AUG</div>
    <h4>Nullam interdum turpis vitae risus vestibulum.</h4>
    <a class="read gold">READ MORE <svg width="16" height="10" viewBox="0 0 16 10" fill="none" stroke="#f3c98b" stroke-width="1.5"><line x1="0" y1="5" x2="15" y2="5"/><polyline points="10,1 15,5 10,9"/></svg></a>
  </article>
  <article class="post" style="left:745px">
    <div class="photo" role="img" aria-label="Hands signing documents on a desk" style="background:linear-gradient(180deg,#6d5c4f,#b9a89a 50%,#e8e1d8)"></div>
    <div class="date">02 AUG</div>
    <h4>Nullam interdum turpis vitae risus vestibulum.</h4>
    <a class="read">READ MORE <svg width="16" height="10" viewBox="0 0 16 10" fill="none" stroke="#232323" stroke-width="1.5"><line x1="0" y1="5" x2="15" y2="5"/><polyline points="10,1 15,5 10,9"/></svg></a>
  </article>
  <div class="btn gold" style="left:530px;top:3464px;width:136px;height:40px">View All</div>

  <!-- Contact -->
  <div class="abs" style="left:210px;top:3691px">
    <div class="eyebrow">Contact Us</div>
    <h2 class="section-title" style="margin-top:4px">Get In Touch</h2>
  </div>
  <div class="abs contact-frame"></div>
  <div class="abs contact-frame2"></div>
  <div class="photo" role="img" aria-label="Two business colleagues reviewing a folder"
       style="left:671px;top:3702px;width:397px;height:395px;background:linear-gradient(160deg,#dfe3e6,#b8c0c6 45%,#5a5f66 80%,#2c2f35)"></div>
  <div class="abs form-box">
    <div class="field" style="left:37px;top:41px;width:206px">Name</div>
    <div class="field" style="left:257px;top:41px;width:208px">Subject</div>
    <div class="field" style="left:37px;top:88px;width:206px">Email</div>
    <div class="field" style="left:257px;top:88px;width:208px">Phone</div>
    <div class="field message" style="left:37px;top:136px;width:428px">Your Message</div>
  </div>
  <div class="btn dark" style="left:247px;top:3986px;width:140px;height:40px">Submit Now</div>

  <!-- Footer -->
  <footer class="abs footer">
    <div class="abs brand" style="left:109px;top:66px">
      <div class="brand-mark" style="width:52px;height:52px"></div>
      <div>
        <div class="brand-name" style="font-size:31px">Brisk Vale</div>
        <div class="brand-sub">GROUP</div>
      </div>
    </div>

    <h5 style="left:409px">Contact Us</h5>
    <div class="contact-row" style="top:114px">
      <svg width="14" height="18" viewBox="0 0 14 18" fill="none" stroke="#f3c98b" stroke-width="1.8"><path d="M7 17s6-6.2 6-10A6 6 0 0 0 1 7c0 3.8 6 10 6 10z"/><circle cx="7" cy="7" r="2.2"/></svg>
      <span>Your Location Name Will Be<br>Here Near This 123456</span>
    </div>
    <div class="contact-row" style="top:164px">
      <svg width="14" height="14" viewBox="0 0 14 14"><path fill="#f3c98b" d="M3 1l2.2 0 1 3-1.5 1.2a8 8 0 0 0 4 4L10 7.7l3 1V11c0 1-1 2-2 2C5.5 13 1 8.5 1 3c0-1 1-2 2-2z"/></svg>
      <span>555 014 2290</span>
    </div>
    <div class="contact-row" style="top:206px">
      <svg width="15" height="12" viewBox="0 0 15 12"><rect width="15" height="12" rx="1.5" fill="#f3c98b"/><polyline points="1,1.5 7.5,7 14,1.5" fill="none" stroke="#232323" stroke-width="1.3"/></svg>
      <span>hello@brisk-vale.com</span>
    </div>

    <h5 style="left:668px">Quick Links</h5>
    <ul class="col-list" style="left:668px;top:104px">
      <li>Home</li><li>About Us</li><li>Team</li><li>Portfolio</li><li>News</li><li>Contact Us</li>
    </ul>

    <h5 style="left:856px">Signup for Newsletter</h5>
    <div class="news-input" style="top:101px">Name:</div>
    <div class="news-input" style="top:150px">Email:</div>
    <div class="btn gold" style="left:856px;top:203px;width:143px;height:40px">Submit Now</div>

    <div class="abs" style="left:109px;top:307px;width:980px;height:1px;background:#3a3a3a"></div>
  </footer>
  <div class="social" style="left:141px" aria-label="Social profile"></div>
  <div class="social" style="left:180px" aria-label="Social profile"></div>
  <div class="social" style="left:221px" aria-label="Social profile"></div>
  <div class="social" style="left:262px" aria-label="Social profile"></div>
  <div class="legal" style="left:109px">©2021 Copyright Brisk Vale Group. All Rights Reserved.</div>
  <div class="legal" style="left:898px">Privacy Policy &nbsp;|&nbsp; Terms &amp; Conditions</div>

</div>
</body>
</html>
```